App Design Project

We are building an app and looking for design help on an existing template. We will also need a style guide. For more information, there is a website which outlines the assignment with visuals. Go here:

http://www.brivolane.com/

Industry/Entity Type

Building

```html
<!DOCTYPE html>
<html lang="en">
<head>
<meta charset="utf-8">
<title>Activities</title>
<link rel="stylesheet" href="https://fonts.googleapis.com/css2?family=Dosis:wght@500;600;700&family=Open+Sans:wght@400;600&display=swap">
<style>
  :root {
    --page-bg: #efe8dc;
    --screen-bg: #c8c3b9;
    --metal-light: #f7f7f7;
    --metal-mid: #dcdcdc;
    --metal-dark: #b9b9b9;
    --teal: #2f9aa6;
    --teal-dark: #1f7c88;
    --teal-light: #8fe6ee;
    --aqua: #6fd8e2;
    --title-grey: #cfd3d6;
    --text-mid: #5b5b5b;
    --white: #ffffff;
  }
  * { box-sizing: border-box; margin: 0; padding: 0; }
  html, body { width: 1200px; height: 966px; overflow: hidden; }
  body { background: var(--page-bg); font-family: "Open Sans", sans-serif; position: relative; }

  .screen {
    position: absolute; left: 349px; top: 35px; width: 502px; height: 896px;
    background: var(--screen-bg);
    box-shadow: 0 2px 6px rgba(0,0,0,.25);
    overflow: hidden;
  }

  .top-bar {
    position: absolute; left: 0; top: 0; width: 502px; height: 97px;
    background: linear-gradient(180deg, var(--metal-light), var(--metal-mid) 60%, var(--metal-dark));
    border-bottom: 1px solid #9d9d9d;
    box-shadow: 0 3px 5px rgba(0,0,0,.25);
  }
  .round-btn {
    position: absolute; top: 11px; width: 82px; height: 82px; border-radius: 50%;
    background: linear-gradient(180deg, #fff, #cfcfcf);
    box-shadow: 0 1px 3px rgba(0,0,0,.3);
  }
  .round-btn span {
    position: absolute; inset: 8px; border-radius: 50%;
    background: radial-gradient(circle at 50% 35%, var(--teal-light), var(--aqua) 60%, #3fbccb);
    display: flex; align-items: center; justify-content: center;
    font-family: "Dosis", sans-serif; font-weight: 600; font-size: 16px; color: var(--teal-dark);
  }
  .round-btn.back { left: 17px; }
  .round-btn.sort { left: 406px; }
  .title-pill {
    position: absolute; left: 141px; top: 14px; width: 220px; height: 75px; border-radius: 38px;
    background: linear-gradient(180deg, #e6e6e6, #fdfdfd 50%, #e2e2e2);
    box-shadow: inset 0 1px 3px rgba(0,0,0,.25), 0 1px 0 #fff;
    display: flex; align-items: center; justify-content: center;
    font-family: "Dosis", sans-serif; font-weight: 600; font-size: 34px; letter-spacing: 1px;
    color: var(--title-grey); text-shadow: 0 1px 1px rgba(0,0,0,.35);
  }

  .filter-tray {
    position: absolute; left: 17px; top: 96px; width: 471px; height: 78px;
    background: linear-gradient(180deg, #d8d8d8, #bdbdbd);
    border: 1px solid #a9a9a9; border-top: none;
    box-shadow: 0 2px 4px rgba(0,0,0,.2);
  }
  .filter-btn {
    position: absolute; top: 18px; width: 132px; height: 44px;
    background: linear-gradient(180deg, #fafafa, #dedede);
    border: 1px solid #9c9c9c; box-shadow: 0 2px 2px rgba(0,0,0,.3);
    display: flex; align-items: center; justify-content: center;
    font-family: "Dosis", sans-serif; font-weight: 600; font-size: 17px; color: var(--text-mid);
  }
  .filter-btn.search { left: 14px; }
  .filter-btn.people { left: 172px; }
  .filter-btn.groups { left: 327px; }

  .activity-card {
    position: absolute; left: 7px; top: 200px; width: 495px; height: 158px;
    background: linear-gradient(180deg, #fbfbfb, #e4e4e4);
    border-radius: 6px 0 0 6px; box-shadow: 0 2px 4px rgba(0,0,0,.3); overflow: hidden;
  }
  .card-head {
    position: absolute; left: 0; top: 0; width: 495px; height: 43px;
    background: linear-gradient(180deg, #3fb2bd, var(--teal));
  }
  .card-title {
    position: absolute; left: 14px; top: 0; height: 43px; line-height: 43px;
    font-family: "Dosis", sans-serif; font-weight: 600; font-size: 26px; color: var(--white); letter-spacing: .5px;
  }
  .expires-label {
    position: absolute; left: 328px; top: 0; width: 123px; height: 43px; line-height: 43px; text-align: center;
    background: var(--teal-dark);
    font-family: "Dosis", sans-serif; font-weight: 600; font-size: 18px; color: #e8f8fa;
  }
  .avatar {
    position: absolute; left: 3px; top: 46px; width: 100px; height: 109px;
    background: linear-gradient(180deg, #9a9a9a, #7c7c7c);
    border-radius: 0 0 0 5px;
  }
  .avatar-name {
    position: absolute; left: 0; bottom: 6px; width: 100%; text-align: center;
    font-size: 15px; font-weight: 600; color: var(--white);
  }
  .event-info {
    position: absolute; left: 117px; top: 57px; font-size: 19px; line-height: 28px; color: var(--text-mid);
  }
  .countdown {
    position: absolute; left: 328px; top: 43px; width: 123px; height: 115px;
    background: linear-gradient(180deg, #f5f5f5, #d6d6d6);
    border-left: 1px solid #a5a5a5; border-right: 1px solid #a5a5a5;
    display: flex; flex-direction: column; align-items: center; justify-content: center;
    font-family: "Dosis", sans-serif; font-weight: 700; font-size: 42px; line-height: 46px;
    color: var(--teal-light); text-shadow: 0 1px 1px var(--teal-dark);
  }
  .card-arrow { position: absolute; left: 457px; top: 80px; }

  .bottom-pill {
    position: absolute; left: 3px; top: 790px; width: 492px; height: 89px; border-radius: 45px;
    background: linear-gradient(180deg, #d6d8d9 0%, #c5cfd1 45%, var(--teal-light) 72%, var(--aqua) 100%);
    border: 2px solid #e8e8e8; box-shadow: 0 2px 4px rgba(0,0,0,.3);
  }
</style>
</head>
<body>
  <main class="screen">
    <header class="top-bar">
      <div class="round-btn back"><span>BACK</span></div>
      <div class="title-pill">ACTIVITIES</div>
      <div class="round-btn sort"><span>SORT</span></div>
    </header>

    <nav class="filter-tray">
      <div class="filter-btn search">SEARCH ALL</div>
      <div class="filter-btn people">PEOPLE</div>
      <div class="filter-btn groups">GROUPS</div>
    </nav>

    <article class="activity-card">
      <div class="card-head">
        <h2 class="card-title">MIDNIGHT VELVET SHOW</h2>
        <div class="expires-label">EXPIRES IN</div>
      </div>
      <div class="avatar" role="img" aria-label="Profile picture of the host">
        <div class="avatar-name">Tessa14</div>
      </div>
      <p class="event-info">Elm Row Cinema<br>October 8, 2012<br>12:00</p>
      <div class="countdown"><span>15H</span><span>39M</span></div>
      <svg class="card-arrow" width="30" height="36" viewBox="0 0 30 36" aria-hidden="true">
        <polyline points="10,8 20,18 10,28" fill="none" stroke="#7a7a7a" stroke-width="4" stroke-linecap="round" stroke-linejoin="round"/>
      </svg>
    </article>

    <div class="bottom-pill"></div>
  </main>
</body>
</html>
```